KELBROOK PAINTING

We are a painting company. We paint residential, commercial and strata jobs. I need the website to be very sharp, neat and elegant. I've attached our logo. the Logo needs to be embossed as a gold color and the background like a Matt black. I need these tabs:

• HOME • ABOUT US • SERVICES • TESTIMONIALS • SHOWCASE • CONTACT US

Be creative and innovative in your style.
take this as an example to just get the gist of what I'm expecting. If you can better it then the job is yours!

http://gilmarchcoatings.com.au/contact.html

I look forward to seeing your artwork :)

#These are the links to my logo in PSD format.

https://www.filevaultzy.com/s/qrtxwpl3k8hvb2z/Kelbrook%20Painting%20Luxury%20Gold.rar

https://www.filevaultzy.com/sh/hvbdkwpa2m7ycq5/XuoP7-bqLk

Painting

• Making the Logo embossed like the artworks i have attached is definitely a necessity.

Can you let me know if this is possible to apply to the website.

thank you

```html
<!DOCTYPE html>
<html lang="en">
<head>
<meta charset="utf-8">
<title>Kelbrook Painting – Our Services</title>
<link href="https://fonts.googleapis.com/css2?family=Source+Sans+3:ital,wght@0,400;0,600;0,700;1,400&display=swap" rel="stylesheet">
<style>
  :root{
    --ink:#1e232b;
    --ink-deep:#181c23;
    --gold:#e8b53e;
    --gold-deep:#d4a01b;
    --gold-mid:#e6b445;
    --gold-soft:#efc678;
    --gold-pale:#f5dca8;
    --slate-1:#4a4f57;
    --slate-2:#7b7f86;
    --slate-3:#a9abad;
    --footer:#a0a1a5;
    --white:#ffffff;
    --text-dark:#2b2f36;
  }
  *{margin:0;padding:0;box-sizing:border-box}
  html,body{width:987px;height:1200px;overflow:hidden;background:var(--ink)}
  body{position:relative;font-family:"Source Sans 3",sans-serif;color:var(--white)}

  .site-header{position:absolute;left:0;top:0;width:987px;height:77px;background:var(--ink);border-bottom:1px solid #8d8a80}
  .phone{position:absolute;right:136px;top:14px;display:flex;align-items:center;gap:8px;color:var(--gold);font-weight:700;font-size:18px}
  .phone svg{width:17px;height:17px}
  .main-nav{position:absolute;right:136px;top:52px;display:flex;gap:25px}
  .main-nav a{color:var(--white);text-decoration:none;font-weight:700;font-size:11.5px;letter-spacing:.4px}
  .main-nav a.is-active{color:var(--gold)}

  .hero{position:absolute;left:0;top:77px;width:987px;height:371px;
    background:linear-gradient(180deg,#6b5242 0%,#5a3e2c 40%,#8c6a52 75%,#b4a092 100%)}
  .hero-dots{position:absolute;right:136px;top:102px;display:flex;gap:8px;z-index:3}
  .hero-dots span{width:7px;height:7px;background:#3b3c40}
  .hero-dots span.is-current{background:var(--gold)}

  .brand-badge{position:absolute;left:142px;top:22px;width:88px;height:88px;border-radius:50%;background:var(--ink);border:3px solid var(--gold-deep);z-index:4}
  .brand-strip{position:absolute;left:232px;top:77px;width:413px;height:32px;
    background:linear-gradient(90deg,#f2d77d,#e8c35a 60%,#f0d98e);display:flex;align-items:center;padding-left:10px;z-index:3}
  .brand-name{color:var(--ink);font-weight:700;font-size:18px;letter-spacing:.8px}
  .brand-sep{width:1px;height:16px;background:#8a6b1e;margin:0 12px}
  .brand-tag{color:var(--ink);font-style:italic;font-size:15px}

  .hero-caption{position:absolute;left:0;top:0}
  .accent-left{position:absolute;left:136px;top:276px;width:46px;height:44px;background:var(--gold)}
  .accent-right{position:absolute;left:546px;top:322px;width:137px;height:84px;background:var(--gold)}
  .caption-box{position:absolute;left:145px;top:284px;width:523px;height:114px;background:var(--ink);padding:14px 0 0 29px;
    font-size:34px;line-height:40px;font-weight:400}
  .caption-tick{position:absolute;left:639px;top:284px;width:29px;height:5px;background:var(--slate-3)}

  .stripe{position:absolute;left:0;width:987px;height:7px;display:flex}
  .stripe span{height:100%}
  .stripe-top{top:448px}
  .stripe-bottom{top:1056px;background:var(--footer)}

  .services{position:absolute;left:0;top:455px;width:987px;height:601px;background:var(--ink)}
  .services-title{position:absolute;left:136px;top:30px;color:var(--gold);font-weight:700;font-size:35px}
  .service{position:absolute;width:225px}
  .service h3{color:var(--gold);font-weight:700;font-size:22.5px;line-height:22.5px;text-transform:uppercase}
  .service p{margin-top:10px;font-size:12px;line-height:22.8px;font-weight:600}

  .site-footer{position:absolute;left:0;top:1063px;width:987px;height:137px;background:var(--footer);color:var(--text-dark)}
  .brands-label{position:absolute;left:138px;top:22px;line-height:1}
  .brands-label strong{display:block;font-size:18.5px;font-weight:400;letter-spacing:.5px}
  .brands-label span{display:block;font-size:12.5px;font-weight:600;margin-top:2px}
  .partner{position:absolute;top:28px;font-weight:700;font-size:20px;color:var(--ink)}
  .copyright{position:absolute;left:138px;top:103px;font-size:10px}
  .social{position:absolute;left:710px;top:97px;display:flex;gap:14px}
  .social span{width:24px;height:24px;border-radius:50%;background:var(--text-dark)}
</style>
</head>
<body>
  <header class="site-header">
    <div class="phone">
      <svg viewBox="0 0 24 24" aria-hidden="true"><path fill="#e8b53e" d="M6.6 10.8c1.4 2.8 3.8 5.1 6.6 6.6l2.2-2.2c.3-.3.7-.4 1-.2 1.1.4 2.3.6 3.6.6.6 0 1 .4 1 1V20c0 .6-.4 1-1 1C10.6 21 3 13.4 3 4c0-.6.4-1 1-1h3.5c.6 0 1 .4 1 1 0 1.3.2 2.5.6 3.6.1.3 0 .7-.2 1L6.6 10.8z"/></svg>
      1300 47 61 92
    </div>
    <nav class="main-nav">
      <a href="#">HOME</a><a href="#">ABOUT US</a><a href="#" class="is-active">SERVICES</a><a href="#">TESTIMONIALS</a><a href="#">SHOWCASE</a><a href="#">CONTACT US</a>
    </nav>
  </header>

  <section class="hero" role="img" aria-label="Photo of a warmly lit living room with a brown and cream curved leather sofa">
    <div class="hero-dots"><span></span><span></span><span></span><span class="is-current"></span></div>
  </section>

  <div class="brand-badge"></div>
  <div class="brand-strip">
    <span class="brand-name">KELBROOK PAINTING</span><span class="brand-sep"></span><span class="brand-tag">Painting Australia Everyday!</span>
  </div>

  <div class="hero-caption">
    <div class="accent-left"></div>
    <div class="accent-right"></div>
    <div class="caption-box">We paint residential,<br>commercial and strata jobs</div>
    <div class="caption-tick"></div>
  </div>

  <div class="stripe stripe-top">
    <span style="width:236px"></span>
    <span style="width:68px;background:var(--slate-1)"></span>
    <span style="width:74px;background:var(--slate-2)"></span>
    <span style="width:116px;background:var(--slate-3)"></span>
    <span style="width:99px;background:var(--gold-deep)"></span>
    <span style="width:68px;background:var(--gold-mid)"></span>
    <span style="width:75px;background:var(--gold-soft)"></span>
    <span style="width:251px;background:var(--gold-pale)"></span>
  </div>

  <main class="services">
    <h2 class="services-title">Our Services</h2>

    <article class="service" style="left:136px;top:119px"><h3>Commercial<br>Painting</h3><p>Lorem ipsum dolor sit amet, consectetur adipiscing elit. Quantum Aristoxeni ingenium consumptum videmus in musicis? Nihil enim hoc differt. Re mihi non aeque satisfacit, et quidem locis pluribus.</p></article>
    <article class="service" style="left:379px;top:119px"><h3>Color<br>Consulting</h3><p>Lorem ipsum dolor sit amet, consectetur adipiscing elit. Quantum Aristoxeni ingenium consumptum videmus in musicis? Nihil enim hoc differt. Re mihi non aeque satisfacit, et quidem locis pluribus.</p></article>
    <article class="service" style="left:622px;top:119px"><h3>Fence<br>Painting</h3><p>Lorem ipsum dolor sit amet, consectetur adipiscing elit. Quantum Aristoxeni ingenium consumptum videmus in musicis? Nihil enim hoc differt. Re mihi non aeque satisfacit, et quidem locis pluribus.</p></article>

    <article class="service" style="left:136px;top:362px"><h3>Exterior Timber<br>Maintenance</h3><p>Lorem ipsum dolor sit amet, consectetur adipiscing elit. Quantum Aristoxeni ingenium consumptum videmus in musicis? Nihil enim hoc differt. Re mihi non aeque satisfacit, et quidem locis pluribus.</p></article>
    <article class="service" style="left:379px;top:362px"><h3>Special<br>Finishes</h3><p>Lorem ipsum dolor sit amet, consectetur adipiscing elit. Quantum Aristoxeni ingenium consumptum videmus in musicis? Nihil enim hoc differt. Re mihi non aeque satisfacit, et quidem locis pluribus.</p></article>
    <article class="service" style="left:622px;top:362px"><h3>Spray<br>Painting</h3><p>Lorem ipsum dolor sit amet, consectetur adipiscing elit. Quantum Aristoxeni ingenium consumptum videmus in musicis? Nihil enim hoc differt. Re mihi non aeque satisfacit, et quidem locis pluribus.</p></article>
  </main>

  <div class="stripe stripe-bottom">
    <span style="width:251px;background:var(--gold-pale)"></span>
    <span style="width:75px;background:var(--gold-soft)"></span>
    <span style="width:68px;background:var(--gold-mid)"></span>
    <span style="width:99px;background:var(--gold-deep)"></span>
    <span style="width:116px;background:var(--slate-3)"></span>
    <span style="width:75px;background:var(--slate-2)"></span>
    <span style="width:67px;background:var(--slate-1)"></span>
  </div>

  <footer class="site-footer">
    <div class="brands-label"><strong>BRANDS</strong><span>USED BY US</span></div>
    <span class="partner" style="left:262px">Corvane</span>
    <span class="partner" style="left:390px">Halstyn</span>
    <span class="partner" style="left:518px">Brentmoor</span>
    <span class="partner" style="left:702px">Veltrax</span>
    <p class="copyright">Copyright @ 2013 Kelbrook Painting. All rights reserved.</p>
    <div class="social"><span></span><span></span><span></span><span></span></div>
  </footer>
</body>
</html>
```